Packaging for Nutrazest Boxes

we need a long term designer to put together box designs for our website nutrazest.example.. the best designer will be hired for long term projects. The first box I want made is for BriteTide for Dr Halloran

Colors
FFC000
F8CF3A
FAE287
FDF2CF
FEFAEE

Requirements
Must have
• Please use the boxes with packets coming out of the slits on www.nutrazest.example as inspiration for this project. For the Bright Tide mockup box- we'd like it to be a yellowish/orangish color & use the logo uploaded on the top left corner of the box and image of Dr. Mina Halloran on the bottom left corner. On the top right corner of the box, please include the text: "Hand chosen supplements from providers I trust for my patients, my family, and myself." The text on the package coming out of the slit should state: 1 Orca Blend, 1 QLM Revalora, 1 Solace Marine 1800, & the Nutrazest logo. This text should be listed on top of each other.

```html
<!DOCTYPE html>
<html lang="en">
<head>
<meta charset="utf-8">
<title>Bright Tide by Dr. Halloran – Box Lid</title>
<link rel="stylesheet" href="https://fonts.googleapis.com/css2?family=Oswald:wght@400;600;700&family=Open+Sans:ital,wght@0,400;0,600;1,400&display=swap">
<style>
  :root {
    --sun-bg: #ffc600;
    --sun-pill: #ffc000;
    --sun-soft: #fae287;
    --lime-bg: #8fb800;
    --lime-pill: #7eaa1c;
    --lime-soft: #c9dc8a;
    --lid-white: #ffffff;
    --packet: #fefaee;
    --slit: #2a2a2a;
    --ink: #1b1b1b;
    --label-ink: #111111;
  }
  * { margin: 0; padding: 0; box-sizing: border-box; }
  html, body { width: 1200px; height: 2400px; overflow: hidden; }
  body { font-family: "Oswald", sans-serif; color: var(--ink); }

  .variant {
    width: 1200px; height: 1200px;
    display: flex; align-items: center; justify-content: center;
  }
  .variant--sun { background: var(--sun-bg); --accent: var(--sun-pill); --soft: var(--sun-soft); }
  .variant--lime { background: var(--lime-bg); --accent: var(--lime-pill); --soft: var(--lime-soft); }

  .lid {
    position: relative;
    width: 880px; height: 620px;
    background: var(--lid-white);
    border-radius: 6px;
  }

  .lid-logo {
    position: absolute; left: 40px; top: 40px;
    display: flex; align-items: center; gap: 12px;
    font-weight: 600; font-size: 30px; line-height: 1;
    color: var(--ink);
  }
  .lid-logo-dot {
    width: 28px; height: 28px; border-radius: 50%;
    background: var(--accent);
  }

  .quote-pill {
    position: absolute; right: 40px; top: 32px;
    width: 420px; height: 84px; border-radius: 42px;
    background: var(--accent);
    display: flex; align-items: center; justify-content: center;
    padding: 0 40px; text-align: center;
    font-family: "Open Sans", sans-serif; font-style: italic;
    font-size: 15px; line-height: 1.35; color: var(--ink);
  }

  .brand-pill {
    position: absolute; left: 170px; top: 140px;
    width: 540px; height: 270px; border-radius: 135px;
    background: var(--accent);
    display: flex; flex-direction: column;
    align-items: center; justify-content: center; text-align: center;
  }
  .brand-name { font-weight: 700; font-size: 70px; line-height: 1; letter-spacing: 0.5px; }
  .brand-doctor { font-weight: 600; font-size: 30px; line-height: 1.1; margin-top: 4px; }
  .product-label {
    margin-top: 14px; padding: 5px 30px; border-radius: 30px;
    background: var(--label-ink); color: var(--accent);
    font-weight: 600; font-size: 24px; letter-spacing: 3px; text-transform: uppercase;
  }
  .product-note {
    margin-top: 10px; width: 380px;
    font-family: "Open Sans", sans-serif; font-size: 14px; line-height: 1.35;
  }

  .doctor-photo {
    position: absolute; left: 40px; top: 440px;
    width: 190px; height: 145px; border-radius: 8px;
    background: linear-gradient(160deg, var(--soft), var(--accent));
  }

  .packet-slot {
    position: absolute; left: 260px; top: 434px;
    width: 580px; height: 151px;
  }
  .packet {
    position: absolute; left: 20px; right: 20px; top: 0; bottom: 5px;
    background: var(--packet);
    border: 2px solid var(--accent);
    border-bottom: none;
    border-radius: 8px 8px 0 0;
    display: flex; flex-direction: column;
    align-items: center; justify-content: center;
    gap: 2px; text-align: center;
  }
  .packet-item { font-weight: 600; font-size: 22px; line-height: 1.2; }
  .packet-brand { font-weight: 600; font-size: 22px; line-height: 1.2; color: var(--accent); }
  .slit {
    position: absolute; left: 0; right: 0; bottom: 0;
    height: 6px; border-radius: 3px; background: var(--slit);
  }
</style>
</head>
<body>

  <section class="variant variant--sun">
    <div class="lid">
      <div class="lid-logo"><span class="lid-logo-dot"></span>Bright Tide</div>
      <p class="quote-pill">“Hand chosen supplements from providers I trust for my patients, my family, and myself.”</p>
      <div class="brand-pill">
        <h1 class="brand-name">Bright Tide</h1>
        <p class="brand-doctor">by Dr. Halloran</p>
        <p class="product-label">Solace Marine 1800</p>
        <p class="product-note">Daily marine support blend for lasting energy and healthy aging.</p>
      </div>
      <div class="doctor-photo" role="img" aria-label="Portrait photo of Dr. Mina Halloran"></div>
      <div class="packet-slot">
        <div class="packet">
          <p class="packet-item">1 Orca Blend</p>
          <p class="packet-item">1 QLM Revalora</p>
          <p class="packet-item">1 Solace Marine 1800</p>
          <p class="packet-brand">Nutrazest</p>
        </div>
        <span class="slit"></span>
      </div>
    </div>
  </section>

  <section class="variant variant--lime">
    <div class="lid">
      <div class="lid-logo"><span class="lid-logo-dot"></span>Bright Tide</div>
      <p class="quote-pill">“Hand chosen supplements from providers I trust for my patients, my family, and myself.”</p>
      <div class="brand-pill">
        <h1 class="brand-name">Bright Tide</h1>
        <p class="brand-doctor">by Dr. Halloran</p>
        <p class="product-label">QLM Revalora</p>
        <p class="product-note">Gentle daily renewal formula for vitality, balance and calm focus.</p>
      </div>
      <div class="doctor-photo" role="img" aria-label="Portrait photo of Dr. Mina Halloran"></div>
      <div class="packet-slot">
        <div class="packet">
          <p class="packet-item">1 Orca Blend</p>
          <p class="packet-item">1 QLM Revalora</p>
          <p class="packet-item">1 Solace Marine 1800</p>
          <p class="packet-brand">Nutrazest</p>
        </div>
        <span class="slit"></span>
      </div>
    </div>
  </section>

</body>
</html>
```